Website for Outdoor Furniture, Sunroom and life style design

I need a website for a company that creates sunroom furniture and design. A sunroom is a room within your home that is surrounded by windows to make it feel like you are outdoors while being indoors to protect you from weather and keep your comfortable.<br/><br/>The company designs and decorates sun rooms for home owners who want to relax and have the feeling of outdoors, while being indoors.

Target Market(s)

home owners, 40+ demographic

Number of Pages Required

5+ page

Requirements
Must have
• See attached zip files for more information including images, copy and descriptions.
• **CONTACT ONLY FROM PIXELBAZAR.COM ALL OTHER FORMS OF COMMUNICATION WILL BE IGNORED**
• COLORS: colors that compliment our logo which is attached here
• Clean, streamlined, easy to navigate.
• No clutter, flashing, bouncing, pop ups.
• Contact info on every page - phone, email, address, hours. Google map somewhere.
• Videos on every page relevant to the content
• Our products are sunrooms and shade but we consider ourselves to be selling a lifestyle. Outdoor living and design.
• Would like to incorporate images of people in our 40 plus demographic to reinforce the lifestyle theme.
• We need the following pages designed (Please see attached zip file for images and sample copy)
• 1. Home: Home page to have prominent area for updating current info like holiday hours, sales, new products, etc
• 2. Sunrooms: See attached zip file for images, text copy etc....
• 3. Shade Solutions: See attached zip file for images, text copy etc....
• 4. Options & Accessories: See attached zip file for images, text copy etc....
• 5. About Us: See attached zip file for images, text copy etc....
• Customer comments/reviews to appear in “bubbles” throughout site
Should not have
• - No search bar
• - No clutter, flashing, bouncing, pop ups.

```html
<!DOCTYPE html>
<html lang="en">
<head>
<meta charset="utf-8">
<title>Solano Sunrooms</title>
<link rel="stylesheet" href="https://fonts.googleapis.com/css2?family=Red+Hat+Display:ital,wght@0,400;0,500;0,600;0,700;1,400&display=swap">
<style>
:root{
  --navy:#15104a;
  --ink:#1c1a3d;
  --text:#6b6b7b;
  --orange:#d9531e;
  --gold:#f0b429;
  --pale:#eef1f7;
  --band:#dfe4ec;
  --map:#e9ebee;
  --white:#ffffff;
}
*{box-sizing:border-box;margin:0;padding:0}
html,body{width:1200px;height:3124px;overflow:hidden}
body{position:relative;background:var(--white);font-family:"Red Hat Display",Arial,sans-serif;color:var(--ink)}
.abs{position:absolute}
.btn-gradient{position:absolute;height:30px;border-radius:15px;background:linear-gradient(90deg,var(--gold),var(--orange));color:#fff;font-size:13px;display:flex;align-items:center;justify-content:center}
.btn-navy{position:absolute;height:30px;border-radius:15px;background:var(--navy);color:#fff;font-size:13px;font-weight:500;display:flex;align-items:center;justify-content:center}
.center{left:0;width:1200px;text-align:center}

/* header */
.site-header{top:0;left:0;width:1200px;height:80px;background:#fff}
.brand{left:87px;top:18px;font-size:22px;font-weight:700;color:var(--navy)}
.tagline{left:87px;top:48px;font-size:9px;color:var(--navy)}
.main-nav{top:31px;left:335px;display:flex;gap:29px;font-size:13.5px;color:var(--ink)}
.main-nav .active{color:var(--orange)}
/* hero */
.hero{top:80px;left:0;width:1200px;height:400px;background:linear-gradient(100deg,#4a3a22 0%,#8a6a3c 35%,#b79a6a 60%,#8e8678 80%,#6f6d6a 100%)}
.hero-title{top:204px;font-size:33.5px;font-weight:600;color:#fff;line-height:39px}
.estimate-band{top:480px;left:0;width:1200px;height:80px;background:var(--band)}
.estimate-flag{top:480px;left:0}
.estimate-label{top:510px;left:127px;font-size:15px;font-weight:600;color:#fff}
.estimate-note{top:511px;left:450px;font-size:13px;font-weight:600;color:var(--ink)}
/* welcome */
.section-title{font-size:33px;font-weight:500;color:var(--navy)}
.welcome-copy{top:681px;left:205px;width:790px;text-align:center;font-size:13.3px;line-height:19.4px;color:var(--text)}
/* services */
.services-bg{top:1004px;left:0;width:1200px;height:368px;background:var(--pale)}
.service-photo{top:924px;width:321px;height:199px}
.service-name{top:1152px;font-size:18px;font-weight:500;color:var(--ink)}
.service-text{top:1182px;width:322px;font-size:13.2px;line-height:19.4px;color:var(--text)}
.read-more{top:1280px;font-size:13.5px;font-weight:600;color:var(--orange)}
/* feature */
.feature-kicker{top:1545px;left:150px;width:396px;text-align:center;font-size:17px;font-weight:500;color:var(--orange)}
.feature-title{top:1575px;left:130px;width:436px;text-align:center;font-size:24px;font-weight:500;line-height:29px;color:var(--navy)}
.feature-frame{top:1452px;left:672px;width:439px;height:319px;border:1.5px solid var(--orange)}
.feature-block{top:1676px;left:672px;width:439px;height:95px;background:var(--orange)}
.feature-photo{top:1484px;left:640px;width:440px;height:256px;background:linear-gradient(160deg,#d9a84a,#c99a45 45%,#5a7a3a 75%,#3e5b2c)}
/* products */
.product-photo{top:1917px;width:232px;height:199px}
.product-label{top:2084px;width:184px;height:63px;background:#fff;box-shadow:0 6px 14px rgba(20,20,60,.12);display:flex;align-items:center;justify-content:center;font-size:15px;font-weight:600;color:var(--ink)}
/* reviews */
.reviews-bg{top:2228px;left:0;width:1200px;height:495px;background:#f2f4f8}
.review-text{top:2419px;left:208px;width:784px;text-align:center;font-size:15.8px;font-style:italic;line-height:24.3px;color:var(--ink)}
.avatar{top:2532px;left:572px;width:56px;height:56px;border-radius:50%;background:linear-gradient(135deg,#6b5a4e,#3a302a)}
.reviewer{top:2606px;font-size:15px;font-weight:600;color:var(--navy)}
.reviewer-role{top:2630px;font-size:12.5px;color:var(--text)}
/* footer */
.site-footer{top:2723px;left:0;width:1200px;height:401px;background:var(--navy)}
.footer-head{top:2801px;font-size:18px;font-weight:500;color:#fff}
.footer-text{font-size:14px;color:#fff;line-height:19px}
.footer-text .hl{color:var(--orange)}
.map{top:2804px;left:616px;width:495px;height:213px;background:var(--map)}
.social{top:2975px;width:40px;height:40px;border-radius:50%;background:#3b3668}
.social.on{background:var(--orange)}
.footer-rule{top:3064px;left:87px;width:1024px;height:1px;background:#3b3668}
.copyright{top:3086px;font-size:11.5px;color:#fff}
.copyright span{color:var(--orange)}
</style>
</head>
<body>

<header class="abs site-header">
  <div class="abs brand">Solano Sunrooms</div>
  <div class="abs tagline">Lakeshore's Sunroom Specialist</div>
  <nav class="abs main-nav">
    <span class="active">-- Home --</span><span>About Us</span><span>Sunrooms</span><span>Shade Solutions</span><span>Options &amp; Accessories</span><span>Reviews</span>
  </nav>
  <div class="btn-gradient" style="left:1000px;top:25px;width:112px">Contact Us</div>
</header>

<section class="abs hero" role="img" aria-label="Sunlit room with window blinds and a potted plant"></section>
<h1 class="abs center hero-title">Explore What Beautiful Window Treatments<br>Can Do For Your Home</h1>
<div class="btn-navy" style="left:504px;top:316px;width:192px">Get A Free Consultation</div>

<div class="abs estimate-band"></div>
<svg class="abs estimate-flag" width="366" height="80" viewBox="0 0 366 80" aria-hidden="true">
  <polygon points="320,0 366,40 320,80 325,80 366,40 325,0" fill="#e9ecf2"/>
  <polygon points="0,0 320,0 362,40 320,80 0,80" fill="#d9531e"/>
</svg>
<div class="abs estimate-label">Get Your Free Estimate</div>
<div class="abs estimate-note">No Credit Card Required - Local Fast Service - Quality Customer Support</div>
<div class="btn-navy" style="left:1000px;top:505px;width:112px">Get A Quote</div>

<h2 class="abs center section-title" style="top:622px">Welcome to Solano</h2>
<p class="abs welcome-copy">We carry a range of sunroom products, from screen rooms to 3 season sunrooms to all season sunrooms. We call ourselves Lakeshore's Sunroom Specialist quite simply because we specialize in sunrooms and sunroom related merchandise and we've been doing it for 30+ years. We don't do windows, doors, siding and roofing with sunrooms on the side. This is what sets us apart from our competitors, our experience and our focus on this particular home renovation category. Let us create a sunroom as individual as you are so that you can start enjoying summer on your terms, not Mother Natures'.</p>
<div class="btn-gradient" style="left:544px;top:812px;width:112px">About Us</div>

<div class="abs services-bg"></div>
<div class="abs service-photo" style="left:87px;background:linear-gradient(160deg,#8fa86a,#b9b09a 50%,#6f6a5a)" role="img" aria-label="Covered patio beside a house"></div>
<div class="abs service-photo" style="left:440px;background:linear-gradient(170deg,#8fbfe8,#e8e8e4 45%,#7a9a4e)" role="img" aria-label="Deck with a white shade roof and flower beds"></div>
<div class="abs service-photo" style="left:792px;background:linear-gradient(160deg,#9aa0a0,#c9cccb 50%,#6a6a66)" role="img" aria-label="Sunroom interior with large windows"></div>

<h3 class="abs service-name" style="left:87px">Sunrooms</h3>
<h3 class="abs service-name" style="left:440px">Shade Solutions</h3>
<h3 class="abs service-name" style="left:792px">Flooring &amp; Accessories</h3>
<p class="abs service-text" style="left:87px">What is a sunroom? What's in it for you, because after all, that's what really matters. Having a sunroom is about bringing the outdoors in. It's about light and airiness and the all important ...</p>
<p class="abs service-text" style="left:440px">Are you getting all of the enjoyment you can from your deck or patio or is it just too hot for you to sit out? If you need some shade, then we have the shade solution that's perfect for you ...</p>
<p class="abs service-text" style="left:792px">Optional options for the sunroom including custom flooring, furniture and other decorations such as railings for stairs and blinds or shades for windows ...</p>
<div class="abs read-more" style="left:87px">Read More &nbsp;→</div>
<div class="abs read-more" style="left:440px">Read More &nbsp;→</div>
<div class="abs read-more" style="left:792px">Read More &nbsp;→</div>

<div class="abs feature-kicker">What We Can Do For You?</div>
<h2 class="abs feature-title">We Creates Sunroom Furniture and Design For Your Home</h2>
<div class="btn-gradient" style="left:268px;top:1660px;width:160px">Get A Free Quote</div>
<div class="abs feature-frame"></div>
<div class="abs feature-block"></div>
<div class="abs feature-photo" role="img" aria-label="Patio with a yellow retractable awning and outdoor furniture"></div>
<svg class="abs" style="left:857px;top:1594px" width="38" height="38" viewBox="0 0 38 38" aria-hidden="true">
  <circle cx="19" cy="19" r="17" fill="none" stroke="#fff" stroke-width="2"/>
  <polygon points="15,11 27,19 15,27" fill="none" stroke="#fff" stroke-width="2" stroke-linejoin="round"/>
</svg>

<h2 class="abs center section-title" style="top:1842px">Our Products</h2>
<div class="abs product-photo" style="left:87px;background:linear-gradient(170deg,#3a4a2a,#8a6a4a 55%,#4a4a48)" role="img" aria-label="Round fire table on a patio"></div>
<div class="abs product-photo" style="left:352px;background:linear-gradient(170deg,#6f8a4a,#a89070 55%,#7a7a78)" role="img" aria-label="Sunroom with tile floor and bistro set"></div>
<div class="abs product-photo" style="left:616px;background:linear-gradient(170deg,#b09a80,#e4ddcc 50%,#6a8a3e)" role="img" aria-label="White vinyl railing on a deck"></div>
<div class="abs product-photo" style="left:879px;background:linear-gradient(170deg,#8a8f8e,#c7cac8 50%,#6a6a66)" role="img" aria-label="Sunroom windows with shades"></div>
<div class="abs product-label" style="left:112px">Fire Tables</div>
<div class="abs product-label" style="left:376px">Floor Covering</div>
<div class="abs product-label" style="left:640px">Railing</div>
<div class="abs product-label" style="left:904px">Sun Shades</div>

<div class="abs reviews-bg"></div>
<h2 class="abs center section-title" style="top:2299px">What Customers Are Saying</h2>
<svg class="abs" style="left:577px;top:2375px" width="46" height="30" viewBox="0 0 46 30" aria-hidden="true">
  <path d="M18 3H8Q3 3 3 9V24Q3 28 8 28H14Q18 28 18 24V18Q18 14 14 14H3M42 3H32Q27 3 27 9V24Q27 28 32 28H38Q42 28 42 24V18Q42 14 38 14H27" fill="none" stroke="#d9531e" stroke-width="3"/>
</svg>
<p class="abs review-text">It is a long established fact that a reader will be distracted by the readable content of a page when looking at its layout. The point of using Lorem Ipsum is that it has a more-or-less normal distribution of letters, as opposed to using 'Content here, content here', making it look like readable English. Many desktop publishing packages and web page editors now use</p>
<svg class="abs" style="left:118px;top:2448px" width="16" height="26" viewBox="0 0 16 26" aria-hidden="true"><path d="M13 2L3 13L13 24" fill="none" stroke="#1c1a3d" stroke-width="2"/></svg>
<svg class="abs" style="left:1066px;top:2448px" width="16" height="26" viewBox="0 0 16 26" aria-hidden="true"><path d="M3 2L13 13L3 24" fill="none" stroke="#1c1a3d" stroke-width="2"/></svg>
<div class="abs avatar" role="img" aria-label="Customer portrait"></div>
<div class="abs center reviewer">Dana Whitley</div>
<div class="abs center reviewer-role">Home owners, Lorem Ipsum</div>

<footer class="abs site-footer"></footer>
<div class="abs footer-head" style="left:87px">Contact Us</div>
<div class="abs footer-head" style="left:351px">Holiday Hours</div>
<div class="abs footer-text" style="left:88px;top:2838px"><span class="hl" style="font-size:16px">Call Us:</span> <span style="font-size:16px">555 014 2290</span><br><span class="hl">e.</span> info@solanosunrooms.com</div>
<div class="abs footer-text" style="left:88px;top:2902px;font-size:13.5px"><span class="hl">Solano Sunrooms:</span> 14 Birch Lane,<br>Maple Ridge, Ontario</div>
<div class="abs footer-text" style="left:352px;top:2840px"><span class="hl" style="font-size:15px">Lakeshore Falls:</span><br><span style="display:block;margin-top:10px;font-size:13.5px">Riverton Home Show<br>March 27 - 29, 2020,</span></div>
<div class="abs footer-text" style="left:352px;top:2922px"><span class="hl" style="font-size:15px">Harbour Arena:</span><br><span style="display:block;margin-top:10px;font-size:13.5px">7 Harbour Way, Riverton<br>March 27 - 29, 2020</span></div>
<div class="abs map" role="img" aria-label="Street map showing the showroom location"></div>
<div class="abs social" style="left:88px"></div>
<div class="abs social on" style="left:136px"></div>
<div class="abs social" style="left:184px"></div>
<div class="abs footer-rule"></div>
<div class="abs center copyright">© 2020 <span>Solano Sunrooms.</span> All Right Reserved</div>

</body>
</html>
```